Business cards for a tribute and obituary website

Our website is called Tribute Lantern.

It is a special place online for people to remember their loved ones who have passed away, through obituaries and tributes. Friends and family can also convey their condolences on the deceased's memorial page. Celebrating the life of the deceased and remembering their legacy is very important to us – death should not be just about grieving.

We would like the card to look tasteful and modern. The design should ideally not have colours that are too bright. The logo and website URL, www.tributelantern.example should be visible on the front of the card, with our slogan "Celebrating a life passed" on the back.

The design should communicate our purpose – remembering loved ones who have passed – and also a lighter tone of celebrating life. It should not look like a funeral director's card!

Our logo has been attached. Looking forward to some beautiful designs! Get creative :)
Updates

Project Deadline Extended
Reason: Thank you all for your designs. The rest of my team and I have not reached a decision on which design to select and I am collecting feedback from them. I will provide feedback for any changes that need to be made soon. It would be great if we could see more original designs and in more colours! We will definitely select a design by this deadline.

Industry/Entity Type

Business

Contact Information for Business Card

Wendy Lumb
Project Manager
614772390
wendylumb@tributelantern.example

Font styles to use
Serif
Sans Serif

Requirements
Must have
• Logo and website address (www.tributelantern.example) on the front.
Nice to have
• Hi designers! It would be nice to see alternative colours – feel free to try out colours that are tasteful and subtle. The colour of the business card does not have to be the same as the logo.
• We would also like to see the logo used in different ways, perhaps a glossy or embossed finish. The card should look stylish.

```html
<!DOCTYPE html>
<html lang="en">
<head>
<meta charset="utf-8">
<title>Tribute Lantern – Business Card</title>
<link href="https://fonts.googleapis.com/css2?family=Roboto+Slab:wght@700&family=Jura:wght@500;600&display=swap" rel="stylesheet">
<style>
  :root {
    --backdrop: #e9e6e1;
    --card-navy: #0c2a49;
    --panel-grey: #5d5e62;
    --panel-rim: #a3a4a8;
    --ink-light: #ffffff;
    --ink-soft: #e4e6ea;
  }
  * { margin: 0; padding: 0; box-sizing: border-box; }
  html, body {
    width: 1200px; height: 899px; overflow: hidden;
    background: var(--backdrop);
  }
  .card {
    position: absolute; left: 100px; top: 160px;
    width: 1000px; height: 580px;
    background: var(--card-navy);
    overflow: hidden;
    box-shadow: 0 14px 34px rgba(0,0,0,0.22);
  }
  .card__panel { position: absolute; inset: 0; width: 1000px; height: 580px; }
  .brand {
    position: absolute; left: 70px; top: 86px;
    display: flex; align-items: center; gap: 22px;
  }
  .brand__dot {
    width: 74px; height: 74px; border-radius: 50%;
    border: 5px solid var(--ink-light);
  }
  .brand__name {
    font-family: "Roboto Slab", serif; font-weight: 700;
    font-size: 50px; line-height: 0.98; color: var(--ink-light);
  }
  .person {
    position: absolute; right: 50px; top: 262px; text-align: right;
    font-family: "Jura", sans-serif; color: var(--ink-light);
  }
  .person__name { font-size: 34px; font-weight: 600; letter-spacing: 1.5px; }
  .person__role { font-size: 20px; font-weight: 500; letter-spacing: 2px; color: var(--ink-soft); margin-top: 2px; }
  .contact {
    position: absolute; left: 70px; top: 292px;
    font-family: "Jura", sans-serif; font-weight: 600;
    color: var(--ink-light);
  }
  .contact__address { font-size: 22px; line-height: 1.3; letter-spacing: 1px; margin-bottom: 10px; }
  .contact__plain { font-size: 21px; letter-spacing: 1px; margin-bottom: 8px; }
  .contact__list { list-style: none; }
  .contact__item {
    display: flex; align-items: center; gap: 12px;
    font-size: 19px; letter-spacing: 0.8px; height: 30px;
  }
  .contact__icon { width: 20px; height: 20px; flex: none; }
</style>
</head>
<body>
  <div class="card">
    <svg class="card__panel" viewBox="0 0 1000 580" aria-hidden="true">
      <path d="M708 0 C640 70 630 300 748 580 L1000 580 L1000 0 Z" fill="var(--panel-rim)"/>
      <path d="M720 0 C652 70 644 300 762 580 L1000 580 L1000 0 Z" fill="var(--panel-grey)"/>
    </svg>

    <div class="brand">
      <span class="brand__dot"></span>
      <div class="brand__name">Tribute<br>Lantern</div>
    </div>

    <div class="person">
      <div class="person__name">WENDY LUMB</div>
      <div class="person__role">PROJECT MANAGER</div>
    </div>

    <div class="contact">
      <p class="contact__address">027.12th floor,Park<br>Crescent Road LKG</p>
      <p class="contact__plain">614 772 390</p>
      <ul class="contact__list">
        <li class="contact__item">
          <svg class="contact__icon" viewBox="0 0 20 20" aria-hidden="true"><path d="M5 2 L8 6 L6.5 8 C7.5 10.5 9.5 12.5 12 13.5 L14 12 L18 15 L16 18 C9 18 2 11 2 4 Z" fill="#fff"/></svg>
          <span>614 772 390</span>
        </li>
        <li class="contact__item">
          <svg class="contact__icon" viewBox="0 0 20 20" aria-hidden="true"><rect x="5" y="1" width="10" height="18" rx="2" fill="none" stroke="#fff" stroke-width="1.8"/><circle cx="10" cy="15.5" r="1.1" fill="#fff"/></svg>
          <span>614 772 390</span>
        </li>
        <li class="contact__item">
          <svg class="contact__icon" viewBox="0 0 20 20" aria-hidden="true"><rect x="5" y="1" width="10" height="6" fill="none" stroke="#fff" stroke-width="1.6"/><rect x="2" y="7" width="16" height="11" rx="1.5" fill="#fff"/><rect x="5" y="10" width="10" height="1.5" fill="var(--card-navy)"/><rect x="5" y="13" width="10" height="1.5" fill="var(--card-navy)"/></svg>
          <span>614 772 390</span>
        </li>
        <li class="contact__item">
          <svg class="contact__icon" viewBox="0 0 20 20" aria-hidden="true"><rect x="1" y="4" width="18" height="12" fill="#fff"/><path d="M1 4 L10 11 L19 4" fill="none" stroke="var(--card-navy)" stroke-width="1.5"/></svg>
          <span>wendylumb@tributelantern.example</span>
        </li>
        <li class="contact__item">
          <svg class="contact__icon" viewBox="0 0 20 20" aria-hidden="true"><circle cx="10" cy="10" r="8.5" fill="none" stroke="#fff" stroke-width="1.6"/><ellipse cx="10" cy="10" rx="3.8" ry="8.5" fill="none" stroke="#fff" stroke-width="1.4"/><path d="M1.5 10 H18.5 M3 6 H17 M3 14 H17" stroke="#fff" stroke-width="1.3"/></svg>
          <span>www.tributelantern.example</span>
        </li>
      </ul>
    </div>
  </div>
</body>
</html>
```